KFL Noblesville Sign

I need to have a sign designed for a new self-storage facility we are going to be opening. The sign will be 4'W X 8'H.

Industry/Entity Type

Self Storage

Requirements
Must have
• Keystone Locker Hub logo at the top of the sign, under the logo I want the rendering.
• I also must have this information on the sign:
• 1. OPENING FALL 2016
• 2. Your premier self-storage facility.
• 3. www.keystonelockerhub.com

```html
<!DOCTYPE html>
<html lang="en">
<head>
<meta charset="utf-8">
<title>Keystone Locker Hub – Opening Fall 2016 Sign</title>
<link rel="stylesheet" href="https://fonts.googleapis.com/css2?family=Archivo+Black&family=Arimo:wght@700&family=Roboto+Condensed:wght@900&display=swap">
<style>
  :root {
    --sign-red: #d4282e;
    --sign-yellow: #fff200;
    --sign-green: #3fae49;
    --sign-green-dark: #25773a;
    --sign-white: #ffffff;
    --render-sky: #cfd6c8;
    --render-wall: #c9b79a;
    --render-grass: #8a9a3c;
  }
  html, body {
    margin: 0;
    padding: 0;
    overflow: hidden;
    background: var(--sign-red);
  }
  .sign {
    position: relative;
    width: 1200px;
    height: 2400px;
    background: var(--sign-red);
    overflow: hidden;
  }
  .sign-bands {
    position: absolute;
    inset: 0;
  }
  .brand-name {
    position: absolute;
    top: 90px;
    left: 0;
    width: 1200px;
    margin: 0;
    text-align: center;
    color: var(--sign-yellow);
    font-family: "Archivo Black", "Arial Black", sans-serif;
    font-weight: 400;
    font-size: 160px;
    line-height: 190px;
    letter-spacing: -2px;
  }
  .headline {
    margin: 0;
  }
  .headline-line {
    position: absolute;
    left: 0;
    width: 1200px;
    text-align: center;
    white-space: nowrap;
    color: var(--sign-yellow);
    font-family: "Roboto Condensed", "Arial Narrow", sans-serif;
    font-weight: 900;
    font-size: 240px;
    line-height: 240px;
    letter-spacing: 2px;
    text-shadow: 8px 8px 0 var(--sign-green-dark);
  }
  .headline-line--opening { top: 1459px; }
  .headline-line--date { top: 1669px; }
  .tagline {
    position: absolute;
    top: 1917px;
    left: 0;
    width: 1200px;
    margin: 0;
    text-align: center;
    white-space: nowrap;
    color: var(--sign-white);
    font-family: "Arimo", Arial, sans-serif;
    font-weight: 700;
    font-size: 74px;
    line-height: 80px;
  }
  .web-address {
    position: absolute;
    top: 2245px;
    left: 0;
    width: 1200px;
    margin: 0;
    text-align: center;
    white-space: nowrap;
    color: var(--sign-white);
    font-family: "Arimo", Arial, sans-serif;
    font-weight: 700;
    font-size: 64px;
    line-height: 80px;
  }
</style>
</head>
<body>
<main class="sign">
  <svg class="sign-bands" width="1200" height="2400" viewBox="0 0 1200 2400" xmlns="http://www.w3.org/2000/svg">
    <defs>
      <linearGradient id="renderingTones" x1="0" y1="0" x2="0" y2="1">
        <stop offset="0" stop-color="#cfd6c8"/>
        <stop offset="0.45" stop-color="#c9b79a"/>
        <stop offset="0.8" stop-color="#c9b79a"/>
        <stop offset="1" stop-color="#8a9a3c"/>
      </linearGradient>
    </defs>
    <path class="edge-band" fill="#fff200"
          d="M0 772 Q600 620 1200 762 L1200 2142 Q600 2262 0 2142 Z"/>
    <path class="rendering" fill="url(#renderingTones)" role="img"
          aria-label="Architectural rendering of the new three-storey self-storage building with green roll-up doors on a lawn under a tree"
          d="M0 792 Q600 644 1200 782 L1200 1298 Q600 1440 0 1298 Z"/>
    <path class="message-panel" fill="#3fae49"
          d="M0 1322 Q600 1464 1200 1322 L1200 2126 Q600 2242 0 2126 Z"/>
  </svg>

  <h1 class="brand-name">Keystone<br>Locker<br>Hub</h1>

  <h2 class="headline">
    <span class="headline-line headline-line--opening">OPENING</span>
    <span class="headline-line headline-line--date">FALL 2016</span>
  </h2>

  <p class="tagline">YOUR PREMIER<br>SELF-STORAGE FACILITY.</p>

  <p class="web-address">www.keystonelockerhub.com</p>
</main>
</body>
</html>
```